Business Card Design Project

Looking for a business card that our customers will remember. We are a high end Travel Agency.
Need a re-memorable classy business card.
Both sides full color.
Must have the following details.
Voyage Harbor Logo (see attached)
4B Wattle Lane
Penhurst Sydney NSW 2241
Phone: 02 9471 3652
Fax: 02 9563 4417
sales@voyageharbor-example.com.au
Consultant Name
Anything else you think we need

```html
<!DOCTYPE html>
<html lang="en">
<head>
<meta charset="utf-8">
<title>Voyage Harbor – Business Card</title>
<link href="https://fonts.googleapis.com/css2?family=Lato:wght@400;700&display=swap" rel="stylesheet">
<style>
  :root {
    --stage: #e4e8ea;
    --paper: #ffffff;
    --brand-blue: #1f5a8f;
    --deep-blue: #0d4f9c;
    --mid-blue: #1b6cc2;
    --ink: #2b2b2b;
    --rule: #1f5a8f;
    --panel-radius: 10px;
  }
  * { box-sizing: border-box; margin: 0; padding: 0; }
  html, body {
    width: 1200px;
    height: 960px;
    overflow: hidden;
    background: var(--stage);
    font-family: "Lato", Arial, sans-serif;
  }
  .sheet {
    width: 1200px;
    height: 960px;
    display: flex;
    flex-direction: column;
    align-items: center;
    justify-content: center;
    gap: 60px;
  }
  .card {
    position: relative;
    width: 560px;
    height: 340px;
    border-radius: 4px;
    overflow: hidden;
    box-shadow: 0 6px 18px rgba(0,0,0,.18);
  }

  /* Front */
  .card--front {
    background: var(--paper);
    padding: 38px 40px;
  }
  .brand {
    display: flex;
    align-items: center;
    gap: 10px;
    color: var(--brand-blue);
    font-weight: 700;
    font-size: 34px;
    letter-spacing: .5px;
  }
  .brand__dot {
    width: 14px;
    height: 14px;
    border-radius: 50%;
    background: var(--brand-blue);
  }
  .consultant { margin-top: 54px; }
  .consultant__name {
    color: var(--brand-blue);
    font-size: 24px;
    font-weight: 400;
    letter-spacing: .3px;
  }
  .consultant__role {
    color: var(--ink);
    font-size: 18px;
    margin-top: 2px;
  }
  .consultant__rule {
    width: 214px;
    height: 2px;
    background: var(--rule);
    margin: 10px 0 12px;
  }
  .contact { list-style: none; color: var(--ink); font-size: 15.5px; line-height: 1.6; }
  .contact__label { color: var(--brand-blue); }
  .contact__sep { color: var(--brand-blue); padding: 0 3px; }
  .contact__web { color: var(--brand-blue); }

  /* Back */
  .card--back {
    background: linear-gradient(160deg, var(--mid-blue) 0%, var(--deep-blue) 100%);
    display: flex;
    align-items: center;
    justify-content: center;
  }
  .back-waves { position: absolute; inset: 0; }
  .back-panel {
    position: relative;
    width: 470px;
    height: 106px;
    background: var(--paper);
    border-radius: var(--panel-radius);
    display: flex;
    align-items: center;
    justify-content: center;
  }
</style>
</head>
<body>
<main class="sheet">
  <section class="card card--front" aria-label="Card front">
    <div class="brand"><span class="brand__dot"></span>Voyage Harbor</div>
    <div class="consultant">
      <h1 class="consultant__name">MARLA QUINN</h1>
      <p class="consultant__role">Consultant</p>
      <div class="consultant__rule"></div>
    </div>
    <ul class="contact">
      <li><span class="contact__label">T:</span> 02 9471 3652<span class="contact__sep">|</span><span class="contact__label">F:</span> 02 9563 4417</li>
      <li><span class="contact__label">E:</span> sales@voyageharbor-example.com.au</li>
      <li class="contact__web">www.voyageharbor-example.com.au</li>
      <li>4B Wattle Lane, Penhurst Sydney NSW 2241</li>
    </ul>
  </section>

  <section class="card card--back" aria-label="Card back">
    <svg class="back-waves" viewBox="0 0 560 340" preserveAspectRatio="none" aria-hidden="true">
      <path d="M0 40 C160 10 380 20 560 80 L560 0 L0 0 Z" fill="#ffffff" opacity=".08"/>
      <path d="M300 340 C380 250 470 200 560 190 L560 340 Z" fill="#ffffff" opacity=".07"/>
      <path d="M0 300 C140 260 260 280 340 340 L0 340 Z" fill="#000000" opacity=".06"/>
    </svg>
    <div class="back-panel">
      <div class="brand"><span class="brand__dot"></span>Voyage Harbor</div>
    </div>
  </section>
</main>
</body>
</html>
```